Movie Poster - Beneath The Amber Tide

Documentary-film poster design.
Attached is a PDF brief with information on what is required and examples of poster designs I like.

The project is a true crime / mystery documentary film. Set in the Soviet Union in 1959.

Colors
3276b5
85abd2
ec1f27

```html
<!DOCTYPE html>
<html lang="en">
<head>
<meta charset="utf-8">
<title>Beneath The Amber Tide – Poster</title>
<link rel="stylesheet" href="https://fonts.googleapis.com/css2?family=Oswald:wght@300;400&family=Rye&family=Rajdhani:wght@500;600&display=swap">
<style>
  :root {
    --page: #ffffff;
    --ink: #000000;
    --paper: #ffffff;
    --blood: #ec1f27;
    --steel: #85abd2;
  }
  * { margin: 0; padding: 0; box-sizing: border-box; }
  html, body { width: 1200px; height: 1199px; overflow: hidden; background: var(--page); }
  .poster {
    position: absolute; left: 239px; top: 90px; width: 720px; height: 1018px;
    background: var(--ink); overflow: hidden; color: var(--paper);
    font-family: "Oswald", "Arial Narrow", sans-serif; font-weight: 300;
  }
  .poster__photo {
    position: absolute; inset: 0;
    background:
      radial-gradient(ellipse 62% 48% at 48% 70%, #e2e2e2 0%, #b3b3b3 35%, #5c5c5c 68%, rgba(0,0,0,0) 100%),
      radial-gradient(ellipse 80% 30% at 50% 40%, #4a4a4a 0%, rgba(0,0,0,0) 100%),
      var(--ink);
  }
  .narrow { display: inline-block; transform: scaleX(0.72); transform-origin: center; white-space: nowrap; }

  .cast { position: absolute; top: 18px; left: 0; width: 100%; }
  .cast__member { position: absolute; transform: translateX(-50%); text-align: center; line-height: 1; white-space: nowrap; }
  .cast__first { display: block; font-size: 15px; }
  .cast__last { font-size: 32px; margin-top: 1px; }

  .title { position: absolute; left: 0; top: 100px; width: 720px; height: 160px; }
  .title text { font-family: "Rye", serif; }
  .subtitle {
    position: absolute; top: 266px; width: 100%; text-align: center;
    font-family: "Rajdhani", sans-serif; font-weight: 500; font-size: 24px; letter-spacing: 0.3px;
  }
  .accent { color: var(--blood); }
  .tagline {
    position: absolute; right: 66px; top: 382px; text-align: right;
    font-family: "Rajdhani", sans-serif; font-weight: 500; font-size: 22px; line-height: 28.5px; letter-spacing: 0.4px;
  }

  .award { position: absolute; top: 750px; width: 120px; height: 64px; transform: translateX(-50%); }
  .award svg { position: absolute; inset: 0; }
  .award__text {
    position: absolute; inset: 0; display: flex; align-items: center; justify-content: center;
    text-align: center; font-size: 22px; line-height: 0.98; color: #f4f4f4;
  }
  .award__text span { display: inline-block; transform: scaleX(0.78); }

  .credit { position: absolute; top: 830px; transform: translateX(-50%); text-align: center; line-height: 1; white-space: nowrap; }
  .credit__role { display: block; font-family: "Rajdhani", sans-serif; font-weight: 600; font-size: 12px; letter-spacing: 0.6px; }
  .credit__name { font-size: 30px; font-weight: 400; }

  .billing { position: absolute; left: 0; width: 100%; text-align: center; font-size: 15px; letter-spacing: 0.2px; white-space: nowrap; }
  .billing .narrow { transform: scaleX(0.8); }
  .billing small { font-size: 10px; }
  .billing sup { font-size: 6px; line-height: 1; display: inline-block; vertical-align: middle; margin-right: 2px; }

  .release { position: absolute; top: 948px; transform: translateX(-50%); font-size: 40px; line-height: 1; letter-spacing: 2px; white-space: nowrap; }
  .site { position: absolute; top: 991px; width: 100%; text-align: center; font-size: 14px; line-height: 1; }
</style>
</head>
<body>
<main class="poster">
  <div class="poster__photo" role="img" aria-label="Grainy black-and-white photograph of a line of hikers with backpacks and ski poles skiing through a snowstorm"></div>

  <div class="cast">
    <div class="cast__member" style="left:158px"><span class="cast__first"><span class="narrow">NAME</span></span><span class="cast__last narrow">SURNAME</span></div>
    <div class="cast__member" style="left:277px"><span class="cast__first"><span class="narrow">NAME</span></span><span class="cast__last narrow">SURNAME</span></div>
    <div class="cast__member" style="left:395px"><span class="cast__first"><span class="narrow">NAME</span></span><span class="cast__last narrow">SURNAME</span></div>
    <div class="cast__member" style="left:536px"><span class="cast__first"><span class="narrow">SPECIAL GUEST</span></span><span class="cast__last narrow">NAME SURNAME</span></div>
  </div>

  <svg class="title" viewBox="0 0 720 160" aria-label="Beneath The Amber Tide">
    <text x="144" y="62" font-size="56" textLength="432" lengthAdjust="spacingAndGlyphs" fill="#fff">BENEATH <tspan fill="#ec1f27">THE</tspan></text>
    <text x="50" y="142" font-size="66" textLength="620" lengthAdjust="spacingAndGlyphs" fill="#fff">AMBER <tspan fill="#ec1f27">TIDE</tspan></text>
  </svg>

  <p class="subtitle">The true story of <span class="accent">the Verkhny Pass Incident</span></p>

  <p class="tagline">Nine dead hikers<br>Sixty years of secrets<br><span class="accent">Russia's</span> greatest mystery uncovered.</p>

  <div class="award" style="left:184px">
    <svg viewBox="0 0 120 64"><path d="M22 8 Q4 32 22 58" stroke="#eee" stroke-width="5" fill="none"/><path d="M98 8 Q116 32 98 58" stroke="#eee" stroke-width="5" fill="none"/></svg>
    <div class="award__text"><span>BEST<br>FEATURE<br>FILM</span></div>
  </div>
  <div class="award" style="left:361px">
    <svg viewBox="0 0 120 64"><path d="M22 12 Q4 34 22 58" stroke="#eee" stroke-width="5" fill="none"/><path d="M98 12 Q116 34 98 58" stroke="#eee" stroke-width="5" fill="none"/></svg>
    <div class="award__text"><span>BEST<br>DIRECTOR</span></div>
  </div>
  <div class="award" style="left:536px">
    <svg viewBox="0 0 120 64"><path d="M22 12 Q4 34 22 58" stroke="#eee" stroke-width="5" fill="none"/><path d="M98 12 Q116 34 98 58" stroke="#eee" stroke-width="5" fill="none"/></svg>
    <div class="award__text"><span>BEST<br>ACTRESS</span></div>
  </div>

  <div class="credit" style="left:182px"><span class="credit__role">DIRECTED BY</span><span class="credit__name narrow">DIRECTOR</span></div>
  <div class="credit" style="left:361px"><span class="credit__role">SCREENPLAY BY</span><span class="credit__name narrow">WRITER</span></div>
  <div class="credit" style="left:534px"><span class="credit__role">STORY BY</span><span class="credit__name narrow">WRITER</span></div>

  <p class="billing" style="top:882px"><span class="narrow">NORTHLIGHT PICTURES <small>PRESENTS A</small> NORTHLIGHT <small>PRODUCTION IN ASSOCIATION WITH</small> STUDIO MERIDIAN ACTOR NAME ACTOR NAME "MOVIE TITLE"</span></p>
  <p class="billing" style="top:904px"><span class="narrow"><sup>CASTING<br>BY</sup>CASTING CREW &nbsp; <sup>MUSIC<br>BY</sup>COMPOSER &nbsp; <sup>COSTUME<br>DESIGNER</sup>COSTUME DESIGNER &nbsp; <sup>EDITED<br>BY</sup>EDITOR &nbsp; <sup>PRODUCTION<br>DESIGNER</sup>PRODUCTION DESIGNER &nbsp; <sup>PRODUCED<br>BY</sup>PRODUCER</span></p>
  <p class="billing" style="top:926px"><span class="narrow"><sup>DIRECTOR OF<br>PHOTOGRAPHY</sup>DIRECTOR OF PHOTOGRAPHY &nbsp; <sup>CO-EXECUTIVE<br>PRODUCER</sup>CO-EXECUTIVE PRODUCER &nbsp; <sup>EXECUTIVE<br>PRODUCER</sup>EXECUTIVE PRODUCER</span></p>

  <p class="release" style="left:286px"><span class="narrow">COMING SOON</span></p>
  <p class="release" style="left:459px"><span class="narrow">MONTH YEAR</span></p>
  <p class="site"><span class="narrow">WWW.AMBERTIDEFILM.COM</span></p>
</main>
</body>
</html>
```